The Lanternfield Evenings - Concert Series Website Design

I've recently decided to launch a concert series in my living room and would love a website to use to promote the series. I'm looking for a simple Wix design that I could take over once it's complete. I'll provide the logo for which I'd like the website to utilize the color scheme.

Target Market(s)

Music lovers in Denver

Industry/Entity Type

Music

Coding

Coded - Design and coding required

Number of Pages Required

2 page

Font styles to use
Script

Requirements
Must have
• 2 pages - one for concert goers to see the schedule and rsvp, and one for artists about the booking process

```html
<!DOCTYPE html>
<html lang="en">
<head>
<meta charset="UTF-8">
<title>The Lanternfield Evenings — Living Room Concert Series</title>
<link rel="stylesheet" href="https://fonts.googleapis.com/css2?family=Josefin+Sans:wght@300;400&family=Poppins:wght@400;500;600&display=swap">
<style>
:root{
  --plum:#5a1a4f;
  --wine:#7a2346;
  --terracotta:#b5574a;
  --cream:#fdf6f2;
  --blush:#fbeeec;
  --ink:#1c1418;
  --muted:#5c5258;
  --white:#ffffff;
  --black:#0c0c0c;
  --grad-button:linear-gradient(90deg,#b5574a 0%,#5a1a4f 100%);
}
*{box-sizing:border-box;margin:0;padding:0}
html,body{width:1200px;height:3928px;overflow:hidden}
body{font-family:"Poppins",sans-serif;color:var(--ink);background:var(--cream)}
.heading-display{font-family:"Josefin Sans",sans-serif;font-weight:300;text-transform:uppercase;letter-spacing:1px;line-height:1.1}
.accent{color:var(--plum)}
.button{display:inline-flex;align-items:center;justify-content:center;border-radius:24px;font-size:14px;font-weight:500;text-decoration:none;height:40px;padding:0 30px}
.button-gradient{background:var(--grad-button);color:var(--white)}

/* header */
.site-header{height:112px;background:var(--cream);display:flex;align-items:center;padding:0 100px 0 120px;position:relative}
.brand{display:flex;align-items:center;gap:10px;text-decoration:none}
.brand-mark{width:40px;height:40px;background:var(--wine);border-radius:4px}
.brand-name{font-family:"Josefin Sans",sans-serif;font-weight:400;font-size:20px;line-height:1.05;color:var(--wine);text-transform:uppercase;width:170px}
.main-nav{display:flex;gap:30px;margin-left:auto;margin-right:60px}
.main-nav a{font-size:15px;font-weight:500;color:var(--ink);text-decoration:none}
.header-cta{height:40px;padding:0 30px;background:linear-gradient(90deg,#7a2346,#5a1a4f)}

/* hero */
.hero{height:648px;position:relative;text-align:center;color:var(--white);
  background:linear-gradient(180deg,#c6796a 0%,#b0604f 30%,#7c3a3b 58%,#3f1c25 85%,#2a1119 100%)}
.hero-inner{position:relative;padding-top:170px}
.hero-title{font-size:52px;letter-spacing:3px}
.hero-sub{font-size:15px;line-height:1.7;margin:24px auto 0;width:620px}
.hero-actions{display:flex;gap:20px;justify-content:center;margin-top:38px}
.button-outline-dark{background:#6d3b44;color:var(--white);border:1px solid rgba(255,255,255,.25)}
.button-light{background:#f4d5b0;color:var(--plum)}

/* intro */
.intro{height:776px;display:flex;padding:128px 100px 0 120px;gap:80px}
.intro-photo{width:444px;height:484px;border-radius:10px;
  background:radial-gradient(circle at 40% 30%,#e7b27a 0%,#b2603c 45%,#4a2a20 100%)}
.intro-text{width:456px;padding-top:0}
.intro-title{font-size:48px;color:var(--ink)}
.intro-text p{font-size:14.5px;line-height:1.75;color:var(--muted);margin-top:28px}
.intro-text p + p{margin-top:30px}
.intro-text .button{margin-top:26px}

/* features */
.features{height:364px;background:linear-gradient(90deg,#b5574a 0%,#8c3a4c 50%,#5a1a4f 100%);display:flex;padding:90px 0 0 148px;gap:110px;color:var(--white)}
.feature{width:240px}
.feature-icon{width:82px;height:82px;border-radius:50%;background:var(--white);display:flex;align-items:center;justify-content:center}
.feature-text{font-size:17px;font-weight:500;line-height:1.6;margin-top:22px}

/* upcoming */
.upcoming{height:600px;text-align:center;padding-top:100px}
.section-title{font-size:48px;color:var(--ink)}
.section-sub{font-size:14.5px;color:var(--muted);margin-top:18px}
.show-cards{display:flex;gap:16px;justify-content:center;margin-top:38px}
.show-card{width:296px;height:368px;background:var(--white);border-radius:8px;overflow:hidden;text-align:left;box-shadow:0 6px 20px rgba(90,26,79,.08)}
.show-photo{height:180px}
.show-photo.one{background:linear-gradient(135deg,#d9863e,#6a3e8c 60%,#2a2240)}
.show-photo.two{background:linear-gradient(135deg,#7a5232,#c58a4a 50%,#3a2516)}
.show-photo.three{background:linear-gradient(135deg,#c77a3a,#7a3a24 55%,#2e1a14)}
.show-body{padding:24px 22px}
.show-body h3{font-size:17px;font-weight:600}
.show-body p{font-size:14px;line-height:1.7;color:var(--muted);margin-top:14px}
.show-body a{display:inline-block;margin-top:10px;font-size:13.5px;font-weight:500;color:var(--ink);text-decoration:underline}

/* past */
.gap-band{height:100px;background:var(--cream)}
.past{height:860px;background:var(--blush);text-align:center;padding-top:104px}
.gallery{position:relative;width:920px;height:492px;margin:60px auto 0}
.gallery-item{position:absolute;border-radius:8px}
.g1{left:0;top:16px;width:300px;height:200px;background:radial-gradient(circle at 30% 40%,#e46aa0,#4a2a6a 60%,#161225)}
.g2{left:312px;top:0;width:300px;height:232px;background:linear-gradient(160deg,#f1b25a,#a2582c 50%,#2a1810)}
.g3{left:624px;top:28px;width:296px;height:196px;background:radial-gradient(circle at 50% 35%,#e06a5a,#6a2a3a 55%,#1a1016)}
.g4{left:0;top:236px;width:300px;height:196px;background:linear-gradient(160deg,#6e8ad0,#3a3a7a 55%,#141428)}
.g5{left:312px;top:244px;width:300px;height:236px;background:linear-gradient(160deg,#f0a04a,#8a4a2a 55%,#241410)}
.g6{left:624px;top:236px;width:296px;height:196px;background:radial-gradient(circle at 50% 40%,#8a6aa0,#2a2040 60%,#0e0c16)}
.past .button{margin-top:56px}

/* footer */
.site-footer{height:468px;background:var(--black);color:var(--white);text-align:center;padding-top:88px}
.footer-title{font-size:46px;letter-spacing:2px}
.footer-sub{font-size:14px;margin-top:20px}
.signup{display:flex;gap:14px;justify-content:center;margin-top:38px}
.signup-field{width:236px;height:40px;border-radius:20px;background:#3a3a3a;color:#d8d8d8;font-size:13px;display:flex;align-items:center;padding-left:24px}
.signup .button{width:150px}
.footer-nav{display:flex;gap:30px;justify-content:center;margin-top:44px}
.footer-nav a{color:var(--white);font-size:14px;font-weight:500;text-decoration:none}
.copyright{font-size:12px;margin-top:22px;color:#d0d0d0}
</style>
</head>
<body>

<header class="site-header">
  <a class="brand" href="#">
    <span class="brand-mark"></span>
    <span class="brand-name">The Lanternfield Evenings</span>
  </a>
  <nav class="main-nav">
    <a href="#">Home</a><a href="#">About Us</a><a href="#">Performances</a><a href="#">Gallery</a><a href="#">Contact Us</a>
  </nav>
  <a class="button header-cta" href="#" style="color:#fff">Get Tickets</a>
</header>

<section class="hero" role="img" aria-label="Mountain range glowing at sunset above a dark pine forest">
  <div class="hero-inner">
    <h1 class="heading-display hero-title">Live music, real moments.<br>Right in our living room.</h1>
    <p class="hero-sub">An intimate living room concert series inspired by the warmth of lantern light and the power of live performance.</p>
    <div class="hero-actions">
      <a class="button button-outline-dark" href="#">View Upcoming Shows</a>
      <a class="button button-light" href="#">Join the Guest List</a>
    </div>
  </div>
</section>

<section class="intro">
  <div class="intro-photo" role="img" aria-label="Concert guests cheering under warm string lights"></div>
  <div class="intro-text">
    <h2 class="heading-display intro-title">An intimate music <span class="accent">experience</span></h2>
    <p>Lorem ipsum dolor sit amet, consectetur adipiscing elit, sed do eiusmod tempor incididunt ut labore et dolore magna aliqua. Ut enim ad minim veniam, quis nostrud exercitation ullamco laboris nisi ut aliquip ex ea commodo consequat. Duis aute irure dolor in reprehenderit in voluptate velit esse cillum dolore eu fugiat nulla pariatur. Excepteur sint occaecat cupidatat non proident, sunt in culpa qui officia deserunt mollit anim id est laborum.</p>
    <p>Lorem ipsum dolor sit amet, consectetur adipiscing elit, sed do eiusmod tempor incididunt ut labore et dolore magna aliqua. Ut enim ad minim veniam.</p>
    <a class="button button-gradient" href="#">Learn More</a>
  </div>
</section>

<section class="features">
  <div class="feature">
    <div class="feature-icon">
      <svg width="44" height="44" viewBox="0 0 44 44" fill="none" stroke="#5a1a4f" stroke-width="2.2" stroke-linecap="round"><circle cx="22" cy="10" r="5"/><path d="M13 24h18M15 24v14M29 24v14M16 18h12"/></svg>
    </div>
    <p class="feature-text">Limited seating for a truly personal experience</p>
  </div>
  <div class="feature">
    <div class="feature-icon">
      <svg width="44" height="44" viewBox="0 0 44 44" fill="none" stroke="#5a1a4f" stroke-width="2.2" stroke-linecap="round"><circle cx="14" cy="11" r="4"/><circle cx="30" cy="11" r="4"/><path d="M8 34V22l8 4 6-3 6 3 8-4v12M16 26l6 4 6-4"/></svg>
    </div>
    <p class="feature-text">Meet &amp; greet opportunities with artists</p>
  </div>
  <div class="feature">
    <div class="feature-icon">
      <svg width="44" height="44" viewBox="0 0 44 44" fill="none" stroke="#5a1a4f" stroke-width="2.2" stroke-linecap="round"><path d="M10 16a12 12 0 0 1 24 0"/><rect x="8" y="16" width="28" height="20" rx="2"/><circle cx="22" cy="26" r="5"/></svg>
    </div>
    <p class="feature-text">High-quality acoustic performances</p>
  </div>
</section>

<section class="upcoming">
  <h2 class="heading-display section-title">Upcoming <span class="accent">performances</span></h2>
  <p class="section-sub">Discover our next featured artists and reserve your seat for an unforgettable evening of live music.</p>
  <div class="show-cards">
    <article class="show-card">
      <div class="show-photo one" role="img" aria-label="Band performing on a stage with colourful lights"></div>
      <div class="show-body"><h3>Heading</h3><p>Discover our next featured artists and reserve your seat for an</p><a href="#">Learn More</a></div>
    </article>
    <article class="show-card">
      <div class="show-photo two" role="img" aria-label="Guitarist playing for a small seated audience"></div>
      <div class="show-body"><h3>Heading</h3><p>Discover our next featured artists and reserve your seat for an</p><a href="#">Learn More</a></div>
    </article>
    <article class="show-card">
      <div class="show-photo three" role="img" aria-label="Acoustic trio performing in a warm living room"></div>
      <div class="show-body"><h3>Heading</h3><p>Discover our next featured artists and reserve your seat for an</p><a href="#">Learn More</a></div>
    </article>
  </div>
</section>

<div class="gap-band"></div>

<section class="past">
  <h2 class="heading-display section-title">Moments from <span class="accent">past evenings</span></h2>
  <div class="gallery">
    <div class="gallery-item g1" role="img" aria-label="Microphone under pink stage lights"></div>
    <div class="gallery-item g2" role="img" aria-label="Band on stage backlit by golden light"></div>
    <div class="gallery-item g3" role="img" aria-label="Singer performing under red light"></div>
    <div class="gallery-item g4" role="img" aria-label="Crowd facing a lit concert stage"></div>
    <div class="gallery-item g5" role="img" aria-label="Audience at a cosy living room show"></div>
    <div class="gallery-item g6" role="img" aria-label="Performer on a dim stage with spotlight"></div>
  </div>
  <a class="button button-gradient" href="#">Learn More</a>
</section>

<footer class="site-footer">
  <h2 class="heading-display footer-title">Be the first to know</h2>
  <p class="footer-sub">Join our mailing list to receive show announcements, early access tickets, and special updates.</p>
  <div class="signup">
    <span class="signup-field">NAME</span>
    <span class="signup-field">EMAIL</span>
    <a class="button button-gradient" href="#">Subscribe</a>
  </div>
  <nav class="footer-nav">
    <a href="#">Home</a><a href="#">About Us</a><a href="#">Performances</a><a href="#">Gallery</a><a href="#">Contact Us</a>
  </nav>
  <p class="copyright">Copyright2025 All Rights Reserved</p>
</footer>

</body>
</html>
```